seeking a modern Business Card design for Roof Plumbering Business

wexcombe roof plumbing is a local metal re-roof and new construction specialist. We are seeking a modern business card to assist with networking within the industry. Our services are predominantly the installation of metal roofs on new houses, however we also do re-roofs when an existing roof needs replacing. We service both residential and commercial properties. Please include the below details on the card:
Name: Owen Wexcombe
Phone: 0471 385 962
Email: owenwexcomberoofing@mailnest.example

Residential & Commercial
Re-roof & New Construction
Fully Insured

I have uploaded our business logo, which we think would suit a black background. Please use all lower case for business name.
Cheers
Updates

Hey Guys, As requested I've uploaded a Pdf version of my logo. Hopefully this help. Thanks

Industry/Entity Type

Business

Contact Information for Business Card

Name: Owen Wexcombe
Phone: 0471 385 962

Residential & Commercial
Fully Insured

Font styles to use
Serif
Sans Serif

Requirements
Must have
• Name must be all lower case "wexcombe roof plumbing"
Nice to have
• Stick with Logo Colours

```html
<!DOCTYPE html>
<html lang="en">
<head>
<meta charset="utf-8">
<title>wexcombe roof plumbing — business card</title>
<link rel="stylesheet" href="https://fonts.googleapis.com/css2?family=Arimo:wght@400;700&display=swap">
<style>
  :root {
    --backdrop: #d9d6d1;
    --card-top: #eef2f4;
    --card-top-edge: #dfe6ea;
    --band-deep: #14587a;
    --band-mid: #1f7aa3;
    --band-light: #2c93bd;
    --band-rule: #3b4a55;
    --brand-blue: #1b6f98;
    --name-ink: #e4edf1;
    --detail-ink: #c9dde6;
    --feature-ink: #a9d3e3;
  }
  * { margin: 0; padding: 0; box-sizing: border-box; }
  html, body {
    width: 1200px;
    height: 969px;
    overflow: hidden;
    background: var(--backdrop);
    font-family: "Arimo", Arial, sans-serif;
  }
  .canvas {
    position: relative;
    width: 1200px;
    height: 969px;
  }
  .card {
    position: absolute;
    left: 75px;
    top: 186px;
    width: 1050px;
    height: 596px;
    background: linear-gradient(180deg, var(--card-top) 0%, var(--card-top-edge) 100%);
    border: 1px solid #c8d2d8;
    overflow: hidden;
  }
  .brand {
    position: absolute;
    left: 58px;
    top: 118px;
    color: var(--brand-blue);
    font-weight: 400;
    display: flex;
    align-items: flex-start;
    gap: 16px;
  }
  .brand-mark {
    width: 22px;
    height: 22px;
    background: var(--brand-blue);
    margin-top: 14px;
  }
  .brand-name {
    display: block;
    font-size: 70px;
    line-height: 1;
    letter-spacing: 1px;
  }
  .brand-sub {
    display: block;
    font-size: 37px;
    line-height: 1.3;
    letter-spacing: 5px;
  }
  .band {
    position: absolute;
    left: 0;
    top: 0;
    width: 1050px;
    height: 596px;
  }
  .contact {
    position: absolute;
    left: 50px;
    top: 360px;
    color: var(--detail-ink);
  }
  .contact-name {
    font-size: 33px;
    font-weight: 700;
    color: var(--name-ink);
    line-height: 1.2;
  }
  .contact-role {
    font-size: 26px;
    line-height: 1.4;
    margin-bottom: 24px;
  }
  .contact-line {
    display: flex;
    align-items: center;
    gap: 10px;
    font-size: 26px;
    line-height: 1.65;
  }
  .contact-line svg { flex: none; }
  .features {
    position: absolute;
    left: 612px;
    top: 440px;
    list-style: none;
    color: var(--feature-ink);
    font-size: 26px;
    line-height: 40px;
  }
  .features li::before {
    content: "";
    display: inline-block;
    width: 7px;
    height: 7px;
    border-radius: 50%;
    background: var(--feature-ink);
    margin: 0 18px 4px 0;
    vertical-align: middle;
  }
</style>
</head>
<body>
<div class="canvas">
  <div class="card">
    <div class="brand">
      <span class="brand-mark"></span>
      <div>
        <span class="brand-name">wexcombe</span>
        <span class="brand-sub">roof plumbing</span>
      </div>
    </div>

    <svg class="band" viewBox="0 0 1050 596" aria-hidden="true">
      <defs>
        <linearGradient id="bandFill" x1="0" y1="0" x2="1" y2="1">
          <stop offset="0" stop-color="#14587a"/>
          <stop offset="0.55" stop-color="#1f7aa3"/>
          <stop offset="1" stop-color="#2c93bd"/>
        </linearGradient>
      </defs>
      <path d="M0 322 H942 L962 344 L982 322 H1050 V596 H0 Z" fill="url(#bandFill)"/>
      <path d="M0 322 H942 L962 344 L982 322 H1050" fill="none" stroke="#3b4a55" stroke-width="5"/>
    </svg>

    <div class="contact">
      <p class="contact-name">Owen Wexcombe</p>
      <p class="contact-role">CEO/Founder</p>
      <p class="contact-line">
        <svg width="26" height="22" viewBox="0 0 26 22" aria-hidden="true">
          <path d="M2 8 C2 2 24 2 24 8 L19 9 L18 6 C15 5 11 5 8 6 L7 9 Z" fill="#c9dde6"/>
          <path d="M7 10 H19 L22 20 H4 Z" fill="#c9dde6"/>
          <circle cx="13" cy="15" r="2.5" fill="#1f7aa3"/>
        </svg>
        0471 385 962
      </p>
      <p class="contact-line">
        <svg width="26" height="20" viewBox="0 0 26 20" aria-hidden="true">
          <rect x="1" y="2" width="24" height="16" fill="#c9dde6"/>
          <path d="M1 2 L13 11 L25 2" fill="none" stroke="#1f7aa3" stroke-width="2"/>
        </svg>
        owenwexcomberoofing@mailnest.example
      </p>
    </div>

    <ul class="features">
      <li>Fully Insured</li>
      <li>Residential &amp; Commercial</li>
      <li>Re-roof &amp; New Construction</li>
    </ul>
  </div>
</div>
</body>
</html>
```